Enhance existing websites

Hello,

With my very limited web design knowledge I have designed my own websites...
Trailquote.example
Rovervalue.example

Whilst I have been very happy with the response I have received I feel the sites need enhancing. Here is what I would like to change..

1, Place a shadow around the whole pages outline so it has a 3d effect with a better background colour.

2, Improve the 'Request a valuation' tab so it stands out, maybe to also insert a curved arrow(s) to direct customer to click 'request a valuation' . Naturally this would need to be done on each page.

3, The testimonials of the 'what customers say' to change every few seconds.

4, The front page image to change every few seconds to a image of my choice.

5, any other suggestions you feel would benefit my site (obviously willing to pay extra for this and within this site)

6, given my limited knowledge my html code will surely need tidying also

7, if possible any changes not to affect my very good google ratings.

Price paid is for both sites as they're practically identical.

Thanks in advance

Glen

```html
<!DOCTYPE html>
<html lang="en">
<head>
<meta charset="utf-8">
<title>Rovervalue.example – Sell your campervan</title>
<link rel="stylesheet" href="https://fonts.googleapis.com/css2?family=Raleway:wght@500;600;700&family=Open+Sans:ital,wght@0,400;0,600;0,700;1,400&display=swap">
<style>
:root{
  --orange:#f7860f;
  --orange-dark:#e0690a;
  --orange-glow:rgba(247,134,15,.45);
  --ink:#444;
  --text:#333;
  --panel:#f0f0f0;
  --quote-bg:#ebebeb;
  --quote-border:#dcdcdc;
  --page-bg:#d9dde2;
  --footer:#333;
  --gold:#c99a00;
  --tick:#2f8a1e;
}
*{box-sizing:border-box;margin:0;padding:0}
html,body{width:999px;height:1200px;overflow:hidden;background:var(--page-bg)}
.stage{position:absolute;left:0;top:0;width:1200px;height:1442px;transform:scale(0.8325);transform-origin:0 0;font-family:Arial,Helvetica,sans-serif;color:var(--text)}
.page{position:absolute;left:100px;top:0;width:1000px;height:1442px;background:#fff;box-shadow:0 0 22px rgba(0,0,0,.28),0 0 4px rgba(0,0,0,.12)}
.abs{position:absolute}
.brand{left:8px;top:16px;font-family:'Raleway',sans-serif;font-weight:700;font-size:35px;color:var(--ink);letter-spacing:.2px}
.brand span{color:var(--orange)}
.tagline{left:8px;top:58px;font-family:'Raleway',sans-serif;font-weight:500;font-size:16px;color:var(--ink)}
.call{right:10px;top:10px;font-family:'Open Sans',sans-serif;font-size:22px;color:#555;letter-spacing:.5px}
.call b{color:var(--orange);font-weight:700}
.nav{right:10px;top:64px;display:flex;font-family:'Open Sans',sans-serif;font-size:14px}
.nav a{display:block;height:28px;line-height:28px;text-decoration:none;color:#777}
.nav .home{background:var(--orange);color:#fff;font-weight:600;width:70px;text-align:center;margin-right:57px}
.nav .hw{margin-right:75px}.nav .faq{margin-right:59px}

.hero{left:10px;top:100px;width:980px;height:425px;overflow:hidden}
.slide{position:absolute;inset:0;animation:fade 18s infinite}
.slide-1{background:linear-gradient(180deg,#9cc3e4 0%,#b9d3e6 22%,#7f9a72 30%,#8fb0c4 40%,#6f8f98 52%,#8c9d8a 62%,#5f9a3a 78%,#4f8f2c 100%)}
.slide-2{background:linear-gradient(180deg,#a9cbe6 0%,#c7dbe9 25%,#8aa47a 38%,#7e9c68 60%,#5b9236 100%);animation-delay:6s;opacity:0}
.slide-3{background:linear-gradient(180deg,#b6d1e8 0%,#d6e3ec 28%,#9aa98a 42%,#6d9a48 70%,#4b8629 100%);animation-delay:12s;opacity:0}
@keyframes fade{0%{opacity:0}5%{opacity:1}33%{opacity:1}38%{opacity:0}100%{opacity:0}}
.slide-1{animation-name:fadefirst}
@keyframes fadefirst{0%{opacity:1}33%{opacity:1}38%{opacity:0}95%{opacity:0}100%{opacity:1}}
.hero h1{position:absolute;left:0;right:0;top:112px;text-align:center;font-family:'Raleway',sans-serif;font-weight:700;font-size:36px;color:#fff;letter-spacing:.5px;text-shadow:0 2px 4px rgba(0,0,0,.7)}
.cta{position:absolute;left:247px;top:308px;width:478px;height:69px;border-radius:8px;background:linear-gradient(#fc9f30,var(--orange-dark));border:2px solid #ffb25c;box-shadow:0 0 0 5px var(--orange-glow),0 4px 10px rgba(0,0,0,.4);font-family:'Open Sans',sans-serif;font-weight:700;font-size:26px;color:#fff;line-height:64px;text-align:center;text-shadow:0 1px 2px rgba(0,0,0,.3);animation:pulse 2.4s ease-in-out infinite}
@keyframes pulse{0%,100%{box-shadow:0 0 0 5px var(--orange-glow),0 4px 10px rgba(0,0,0,.4)}50%{box-shadow:0 0 0 11px rgba(247,134,15,.15),0 4px 10px rgba(0,0,0,.4)}}
.arrow{position:absolute;top:262px}
.arrow-left{left:120px}
.arrow-right{left:752px}
.dots{position:absolute;left:0;right:0;bottom:14px;display:flex;justify-content:center;gap:8px}
.dot{width:10px;height:10px;border-radius:50%;background:rgba(255,255,255,.55);border:1px solid rgba(0,0,0,.25)}
.dot.on{background:#fff}

.welcome{left:12px;top:540px;font-family:'Raleway',sans-serif;font-weight:700;font-size:31px;color:var(--ink)}
.welcome span{color:var(--orange)}
.intro{left:12px;top:583px;width:668px;font-size:12.4px;line-height:18px;color:#333}
.intro p+p{margin-top:18px}
.perks{left:14px;top:762px;list-style:none;font-size:14.5px;color:#222}
.perks li{height:36px;display:flex;align-items:center}
.perks svg{margin-right:10px}
.collect{left:702px;top:555px;width:288px;height:367px;background:var(--panel)}
.collect h2{position:absolute;left:17px;top:4px;font-family:'Raleway',sans-serif;font-weight:700;font-size:31px;color:var(--orange)}
.collect p{position:absolute;left:19px;top:45px;width:255px;font-size:12.4px;line-height:18px;color:#333}
.flag{position:absolute;left:23px;top:92px;width:258px;height:142px;background:linear-gradient(180deg,#5a5f9e,#9a4a64)}
.cities{position:absolute;left:18px;top:246px;display:grid;grid-template-columns:104px 93px 80px;row-gap:5px;font-size:12.4px;line-height:15px;color:#222}
.rule{left:12px;top:947px;width:975px;border-top:1px dotted #aaa}
.say{left:25px;top:964px;font-family:'Raleway',sans-serif;font-weight:700;font-size:30px;color:var(--ink)}
.quote{position:absolute;top:1016px;width:461px;height:111px;background:var(--quote-bg);border:3px solid var(--quote-border);border-radius:8px}
.quote .photo{position:absolute;left:10px;top:13px;width:82px;height:80px;border:3px solid #fff;border-radius:6px;background:linear-gradient(#d8d8d8,#9a9a9a)}
.quote blockquote{position:absolute;left:108px;top:12px;width:335px;font-family:'Open Sans',sans-serif;font-style:italic;font-size:12px;line-height:15.6px;color:#888}
.tail{position:absolute;left:14px;top:108px}
.who{position:absolute;top:1141px;font-family:'Open Sans',sans-serif;font-size:12px;color:#777}
.who b{color:var(--gold);font-weight:600;font-size:13px;margin-right:5px}
.who svg{margin-right:4px;vertical-align:-1px}
.qdots{left:460px;top:1172px;display:flex;gap:8px}
.qdots .dot{border-color:#ccc;background:#ddd}
.qdots .dot.on{background:var(--orange);border-color:var(--orange)}
.makers{left:20px;top:1214px;width:960px;height:100px;background:linear-gradient(90deg,rgba(255,255,255,0),#f7f7f7 20%,#f7f7f7 80%,rgba(255,255,255,0));display:flex;align-items:center;gap:13px;padding-left:12px}
.mk{flex:none}
.footer{left:0;top:1346px;width:1000px;height:96px;background:var(--footer)}
.footer .fbrand{position:absolute;left:19px;top:14px;font-family:'Raleway',sans-serif;font-weight:700;font-size:35px;color:#777}
.footer .ftag{position:absolute;left:19px;top:56px;font-family:'Raleway',sans-serif;font-weight:500;font-size:16px;color:#777}
.footer .flinks{position:absolute;right:18px;top:27px;font-size:13px;font-weight:700;color:#fff;word-spacing:2px}
.footer .faddr{position:absolute;right:18px;top:53px;font-size:12.5px;font-weight:700;color:#fff}
</style>
</head>
<body>
<div class="stage">
  <div class="page">
    <div class="abs brand">Rovervalue<span>.example</span></div>
    <div class="abs tagline">The UK's largest buyer of campervans</div>
    <div class="abs call">Call us on <b>0800 000 4417</b></div>
    <nav class="abs nav">
      <a class="home">Home</a><a class="hw">How it Works</a><a class="faq">FAQ's</a><a>Contact us</a>
    </nav>

    <section class="abs hero">
      <div class="slide slide-1" role="img" aria-label="Photo of caravans parked on a lakeside campsite with hills behind"></div>
      <div class="slide slide-2" role="img" aria-label="Photo of a campervan on a green field"></div>
      <div class="slide slide-3" role="img" aria-label="Photo of a caravan park in the countryside"></div>
      <h1>SELL YOUR CAMPERV&nbsp; QUICKLY AND SECURELY</h1>
      <svg class="arrow arrow-left" width="120" height="90" viewBox="0 0 120 90"><path d="M8 8C20 60 60 78 108 72" fill="none" stroke="#fff" stroke-width="5" stroke-linecap="round"/><path d="M94 60l16 12-17 11" fill="none" stroke="#fff" stroke-width="5" stroke-linecap="round" stroke-linejoin="round"/></svg>
      <svg class="arrow arrow-right" width="120" height="90" viewBox="0 0 120 90"><path d="M112 8C100 60 60 78 12 72" fill="none" stroke="#fff" stroke-width="5" stroke-linecap="round"/><path d="M26 60L10 72l17 11" fill="none" stroke="#fff" stroke-width="5" stroke-linecap="round" stroke-linejoin="round"/></svg>
      <div class="cta">Request a FREE Caravan Valuation</div>
      <div class="dots"><span class="dot on"></span><span class="dot"></span><span class="dot"></span></div>
    </section>

    <h2 class="abs welcome">Welcome to Rover<span>value</span></h2>
    <div class="abs intro">
      <p>Selling your caravan to trailquote.example saves you the usual headaches and costs associated with selling a caravan, not to mention the potential risks involved. All you need to do is either call us on the freephone number provided, or click the button above and complete our online request form with details of your caravan. We will get back to you as soon as possible with a price and a no obligation offer to buy your caravan. If you accept our offer, we'll contact you to collect your caravan at your convenience - free of charge.</p>
      <p>It is our aim to make the process of selling your caravan completely straightforward and hassle-free. From your initial enquiry, to having your caravan sold with money in your bank account or cash in your hand, can take less than 24 hours. We have even managed to complete some transactions the very same day the offer was received.</p>
    </div>
    <ul class="abs perks">
      <li><svg width="21" height="20" viewBox="0 0 21 20"><path d="M1 11l6 7L20 2" fill="none" stroke="var(--tick)" stroke-width="3" stroke-linecap="round"/></svg>Genuine online or verbal offer to purchase</li>
      <li><svg width="21" height="20" viewBox="0 0 21 20"><path d="M1 11l6 7L20 2" fill="none" stroke="var(--tick)" stroke-width="3" stroke-linecap="round"/></svg>Excellent prices offered and paid</li>
      <li><svg width="21" height="20" viewBox="0 0 21 20"><path d="M1 11l6 7L20 2" fill="none" stroke="var(--tick)" stroke-width="3" stroke-linecap="round"/></svg>No admin fees or hidden charges</li>
      <li><svg width="21" height="20" viewBox="0 0 21 20"><path d="M1 11l6 7L20 2" fill="none" stroke="var(--tick)" stroke-width="3" stroke-linecap="round"/></svg>Friendly professional, no hassle service</li>
      <li><svg width="21" height="20" viewBox="0 0 21 20"><path d="M1 11l6 7L20 2" fill="none" stroke="var(--tick)" stroke-width="3" stroke-linecap="round"/></svg>Instant cash or faster payment bank transfer</li>
    </ul>

    <aside class="abs collect">
      <h2>Free Collection</h2>
      <p>Below are some examples of&nbsp; of the areas we cover ...</p>
      <div class="flag" role="img" aria-label="Illustration of the Union flag"></div>
      <div class="cities">
        <span>Birmingham</span><span>Exeter</span><span>Manchester</span>
        <span>Cambridge</span><span>Hertford</span><span>Norwich</span>
        <span>Chelmsford</span><span>Leominster</span><span>Swansea</span>
        <span>Chichester</span><span>Lincoln</span><span>Truro</span>
        <span>Chester</span><span>Maidstone</span><span>Wakefield</span>
      </div>
    </aside>

    <div class="abs rule"></div>
    <h2 class="abs say">What our customers say....</h2>

    <div class="quote" style="left:30px">
      <div class="photo" role="img" aria-label="Customer portrait photo"></div>
      <blockquote>Aenean sed nulla mattis augue pulvinar varius. Pletesque habitant morbi tristique senectus et netus et malesuada fames ac turpis egestas. Vestibulum pharetra sapien a libero congue sed porta nulla sodales.Pellentesqu abitant lesuada fames ac turpis egestas.</blockquote>
      <svg class="tail" width="22" height="26" viewBox="0 0 22 26"><path d="M0 0h22L18 24z" fill="var(--quote-bg)" stroke="var(--quote-border)" stroke-width="3"/><path d="M1 0h19" stroke="var(--quote-bg)" stroke-width="4"/></svg>
    </div>
    <div class="who" style="left:72px"><svg width="7" height="10"><path d="M0 0l7 5-7 5z" fill="#7aa81e"/></svg><b>Marlo Dane,</b> SEO Maven, Co-Creator of Slow Ripple Labs</div>

    <div class="quote" style="left:524px">
      <div class="photo" role="img" aria-label="Customer portrait photo"></div>
      <blockquote>Aenean sed nulla mattis augue pulvinar varius. Peetesque habitant morbi tristique senectus et netus et malesuada fames ac turpis egestas. Vestibulum pharetra sapien a libero congue sed porta nulla sodales.Pellentesqu abitant lesuada fames ac turpis egestas.</blockquote>
      <svg class="tail" width="22" height="26" viewBox="0 0 22 26"><path d="M0 0h22L18 24z" fill="var(--quote-bg)" stroke="var(--quote-border)" stroke-width="3"/><path d="M1 0h19" stroke="var(--quote-bg)" stroke-width="4"/></svg>
    </div>
    <div class="who" style="left:566px"><svg width="7" height="10"><path d="M0 0l7 5-7 5z" fill="#7aa81e"/></svg><b>Marlo Dane,</b> SEO Maven, Co-Creator of Slow Ripple Labs</div>
    <div class="abs qdots"><span class="dot on"></span><span class="dot"></span><span class="dot"></span></div>

    <div class="abs makers" aria-label="Manufacturers we buy">
      <svg class="mk" width="56" height="56"><circle cx="28" cy="28" r="27" fill="#a61c24"/></svg>
      <svg class="mk" width="42" height="52"><rect width="42" height="52" rx="4" fill="#2e5aa8"/></svg>
      <svg class="mk" width="64" height="24"><rect width="64" height="24" rx="4" fill="#b8c2cc"/></svg>
      <svg class="mk" width="52" height="52"><rect width="52" height="52" rx="4" fill="#22a9b5"/></svg>
      <svg class="mk" width="58" height="34"><rect width="58" height="34" rx="4" fill="#9aa3ad"/></svg>
      <svg class="mk" width="50" height="50"><circle cx="25" cy="25" r="24" fill="#555"/></svg>
      <svg class="mk" width="62" height="16"><rect width="62" height="16" rx="3" fill="#2d3e9a"/></svg>
      <svg class="mk" width="38" height="38"><circle cx="19" cy="19" r="18" fill="#d2211f"/></svg>
      <svg class="mk" width="62" height="38"><rect width="62" height="38" rx="19" fill="#2c5a9c"/></svg>
      <svg class="mk" width="42" height="50"><rect width="42" height="50" rx="4" fill="#d7261e"/></svg>
      <svg class="mk" width="62" height="42"><rect width="62" height="42" rx="4" fill="#d23a2e"/></svg>
      <svg class="mk" width="50" height="54"><rect width="50" height="54" rx="4" fill="#3c6fc4"/></svg>
      <svg class="mk" width="64" height="20"><rect width="64" height="20" rx="3" fill="#c92a2a"/></svg>
      <svg class="mk" width="42" height="50"><rect width="42" height="50" rx="4" fill="#8a1e3c"/></svg>
    </div>

    <footer class="abs footer">
      <div class="fbrand">Rovervalue.example</div>
      <div class="ftag">The UK's largest buyer of campervans</div>
      <div class="flinks">Home &nbsp; | &nbsp; How it Works &nbsp; | &nbsp; FAQ's &nbsp; | &nbsp; Contact us</div>
      <div class="faddr">Trailquote.example - Meadow Lane&nbsp; - Elmford&nbsp; - Essex CM00 1AB</div>
    </footer>
  </div>
</div>
</body>
</html>
```